Yard Sign Design for Roofing Contractor

We are looking for a new design for our yard signs used on all jobs we build. We are looking for a way to brand the company and are hoping that this contest can give us a "theme" we can incorporate into out other marketing items such as, vehicle graphics, apparel, etc... I have attached a copy of our logo to be used on the sign, it can be "shadowed" with a color to enhance the look and the sign, but please keep the basic logo design. Attached are some samples of construction colors the boss was thinking of along with a picture of our current yard sign to help give some direction and let you know what info is needed on the sign.The darker construction yellow may work better than the fluorescent yellow, but won't know without visual aid. We are not tied to any particular color as of now, so they do have freedom of design as long as keeping with the construction feel. (Just another thought, potentially a reflective construction tape look would be interesting so signs are visable at night)
Updates

Reason: Meeting with new web designers next week to discuss best option to incorporate into our website.Thank you for the submissions!

Target Market(s)

Want signs to stand out when driving by and visibility in neighborhood where sign is posted for potential referrals

Industry/Entity Type

Contractor

Colors
fbed22
fece3e
f37122

Requirements
Must have
• Information that is on our current signs, image attached. I uploaded a .pdf file showing some options that could work for adding "shading" to our logo if you choose to do so.
• Sign should measure 18" T, 24" W
Nice to have
• Interested is seeing designs using construction tape look, images attached

```html
<!DOCTYPE html>
<html lang="en">
<head>
<meta charset="utf-8">
<title>Tallon Construction Yard Sign</title>
<link rel="stylesheet" href="https://fonts.googleapis.com/css2?family=Archivo+Black&family=Cinzel:wght@700;900&family=Marcellus+SC&family=Arimo:wght@700&display=swap">
<style>
  :root {
    --tape-yellow: #fece3e;
    --tape-black: #1a1208;
    --sign-yellow: #fbed22;
    --ink: #0d0b08;
    --paper: #ffffff;
  }
  html, body {
    margin: 0;
    padding: 0;
    width: 1200px;
    height: 900px;
    overflow: hidden;
    background: var(--paper);
  }
  .sign {
    position: relative;
    width: 1200px;
    height: 900px;
    overflow: hidden;
  }
  .tape-border {
    position: absolute;
    inset: 0;
    background: repeating-linear-gradient(
      45deg,
      var(--tape-yellow) 0 30px,
      var(--tape-black) 30px 60px
    );
  }
  .panel {
    position: absolute;
    left: 56px;
    top: 56px;
    width: 1091px;
    height: 667px;
    background: var(--paper);
    overflow: hidden;
  }
  .award-corner {
    position: absolute;
    left: 0;
    top: 0;
  }
  .award-text {
    position: absolute;
    left: 185px;
    top: 125px;
    margin: 0;
    font-family: "Archivo Black", sans-serif;
    font-size: 54px;
    line-height: 0.95;
    color: var(--ink);
    text-align: center;
    white-space: nowrap;
    transform: translate(-50%, -50%) rotate(-27deg);
  }
  .accreditation-badge {
    position: absolute;
    right: 45px;
    top: 21px;
    width: 97px;
    height: 157px;
    border-radius: 10px;
    background: var(--ink);
  }
  .website {
    position: absolute;
    left: 0;
    right: 0;
    top: 188px;
    margin: 0;
    text-align: center;
    font-family: "Arimo", sans-serif;
    font-weight: 700;
    font-size: 56px;
    line-height: 1;
    color: var(--ink);
  }
  .company-name {
    margin: 0;
    font-weight: normal;
  }
  .name-main,
  .name-sub {
    position: absolute;
    left: 0;
    right: 0;
    text-align: center;
    font-family: "Cinzel", serif;
    color: var(--ink);
    line-height: 1;
    white-space: nowrap;
  }
  .name-main {
    top: 258px;
    font-size: 172px;
    font-weight: 900;
  }
  .name-sub {
    top: 466px;
    font-size: 84px;
    font-weight: 700;
  }
  .services {
    position: absolute;
    left: 0;
    right: 0;
    top: 596px;
    margin: 0;
    text-align: center;
    font-family: "Marcellus SC", serif;
    font-size: 58px;
    line-height: 1;
    color: var(--ink);
    word-spacing: 10px;
    letter-spacing: 2px;
  }
  .phone-band {
    position: absolute;
    left: 0;
    top: 723px;
    width: 1200px;
    height: 121px;
    background: var(--ink);
    display: flex;
    align-items: center;
    justify-content: center;
  }
  .phone {
    margin: 0;
    font-family: "Archivo Black", sans-serif;
    font-size: 118px;
    letter-spacing: 3px;
    color: var(--sign-yellow);
    line-height: 1;
  }
</style>
</head>
<body>
  <main class="sign">
    <div class="tape-border" aria-hidden="true"></div>

    <section class="panel">
      <svg class="award-corner" width="620" height="340" viewBox="0 0 620 340" aria-hidden="true">
        <polygon points="0,0 600,0 0,310" fill="var(--sign-yellow)"/>
      </svg>
      <p class="award-text">AWARD<br>WINNING!</p>

      <div class="accreditation-badge" aria-hidden="true"></div>

      <p class="website">www.tallonroofing.com</p>

      <h1 class="company-name">
        <span class="name-main">TALLON</span>
        <span class="name-sub">CONSTRUCTION</span>
      </h1>

      <p class="services">ROOF &bull; SIDING &bull; GUTTERS</p>
    </section>

    <div class="phone-band">
      <p class="phone">405-555-0142</p>
    </div>
  </main>
</body>
</html>
```